■依頼の目的
2月に出版予定の電子書籍

タイトル:後悔しない住まい手配ガイド決定版2021
サブタイトル:[特集]三世代でつなぐ暮らし設計
著者:一級建築士 柚木湊

キャッチコピー:コロナ対応住宅チェックリスト付き!

※追加テキスト
家づくりの補助金
4月に省エネ説明義務化
IoT住宅の現在

キャッチコピー等の配置はPDFに記載

の表紙デザインをお願いします。

■本の内容
・年一回発行する雑誌形式の電子書籍
・住宅会社選びの方法を紹介
・特集記事や時事ネタも扱う

■デザイン要望
・30代~40代の子育て夫婦に好まれるデザインを希望
・LivoMarqueのようなお洒落な家づくり雑誌の雰囲気
・過去の4作品との差別化(過去表紙はPDFに)
・最新作であることがわかるよう「2021」を目立つように

■キャッチ等の変更の可能性あり
お願いする方が決まった後、キャッチコピーなどの文字を若干変更する可能性があります。

■添付ファイルについて
・必要な配置をPDFに添付しています
・ロゴのaiデータ添付します

その他何かご不明な点がございましたら、お気軽にご質問下さい。
よろしくお願いいたします。
・Pebble magazine というタイトルの色は、変えるようにしてください。
年一回の雑誌なので、毎年、ちがう色を使っています。
過去の作品と被らないように色提案をお願いします。
・文字はスマホで見た時にも、読めることを意識してください。
・背景の写真・イラストのセレクトが重要になります。livoなどのインテリア雑誌などを参考にしてください。

写真の選び方が秀逸でした。
シンメトリーを意識したモダンな建物外観が素晴らしく、それを引き立たせるようなデザインで、見た瞬間、これしかないと思わせるものでした。
今回は、私のメルマガ読者200人にアンケートを行って半数の方がこのデザインを支持しました。

この度は、沢山のご提案を頂きありがとうございました!
毎年、出版しているシリーズでしたが、雰囲気を一新したいことからコンペを使わせて頂きましたが、様々なデザイン提案を頂き、とても参考になりました。
今後もコンペを使わせて頂きますので、引き続きよろしくお願いいたします!

```html
<!DOCTYPE html>
<html lang="ja">
<head>
<meta charset="utf-8">
<title>Pebble magazine vol.4 2021</title>
<link rel="stylesheet" href="https://fonts.googleapis.com/css2?family=Noto+Sans+JP:wght@500;700;900&family=Playfair+Display:ital,wght@0,700;0,900;1,400&display=swap">
<style>
  :root {
    --ink: #1b1b1b;
    --logo-brown: #6b4a32;
    --paper: #ffffff;
    --wall-top: #f4f3f1;
    --wall-mid: #e6e3de;
    --sofa: #d9d3cb;
    --wood: #8a5a38;
    --wood-dark: #4e301c;
    --rule: #6b4a32;
  }
  * { margin: 0; padding: 0; box-sizing: border-box; }
  html, body { width: 750px; height: 1200px; overflow: hidden; background: var(--paper); }
  .cover {
    position: relative;
    width: 750px; height: 1200px;
    overflow: hidden;
    font-family: "Noto Sans JP", sans-serif;
    color: var(--ink);
  }
  .cover-photo {
    position: absolute; inset: 0;
    background:
      radial-gradient(ellipse 60% 18% at 50% 68%, rgba(200,190,178,.55), transparent 70%),
      linear-gradient(180deg, var(--wall-top) 0%, var(--wall-top) 40%, var(--wall-mid) 55%, var(--sofa) 66%, #b9a48f 74%, var(--wood) 82%, var(--wood-dark) 100%);
  }
  .masthead { position: absolute; left: 30px; top: 14px; }
  .masthead-kana { font-size: 15px; font-weight: 500; color: var(--logo-brown); letter-spacing: .05em; }
  .masthead-name {
    font-family: "Playfair Display", serif; font-weight: 700;
    color: var(--logo-brown); line-height: .95;
  }
  .masthead-name .word-main { display: block; font-size: 104px; }
  .masthead-name .word-sub { display: block; font-size: 52px; padding-left: 18px; }
  .masthead-issue {
    position: absolute; left: 190px; top: 4px;
    font-family: "Playfair Display", serif; font-size: 15px; color: var(--logo-brown);
  }
  .topics {
    position: absolute; right: 22px; top: 70px; width: 270px;
    list-style: none;
  }
  .topics li {
    font-size: 27px; font-weight: 700; line-height: 1;
    padding: 20px 0 16px; border-bottom: 2px solid var(--rule);
    text-align: right; letter-spacing: -.02em; white-space: nowrap;
  }
  .topics li:last-child { border-bottom: none; }
  .title {
    position: absolute; left: 0; right: 0; top: 290px;
    text-align: center; font-weight: 900;
    font-size: 104px; line-height: 1.17; letter-spacing: -.02em;
    text-shadow: 0 0 14px rgba(255,255,255,.9);
  }
  .title-line { display: block; }
  .title-en {
    position: absolute; left: 30px; top: 680px; width: 190px;
    font-family: "Playfair Display", serif; font-style: italic;
    font-size: 17px; line-height: 1.25; color: var(--ink);
  }
  .title-year {
    position: absolute; left: 0; right: 0; top: 820px;
    text-align: center;
    font-family: "Playfair Display", serif; font-weight: 900;
    font-size: 200px; line-height: 1; color: var(--paper);
    text-shadow: 0 4px 10px rgba(0,0,0,.35);
    letter-spacing: .02em;
  }
  .badge {
    position: absolute; left: 530px; top: 820px;
    width: 200px; height: 200px; border-radius: 50%;
    background: var(--paper);
    display: flex; flex-direction: column; align-items: center; justify-content: center;
    text-align: center; font-weight: 900; font-size: 26px; line-height: 1.25;
    box-shadow: 0 3px 10px rgba(0,0,0,.25);
  }
  .badge svg { margin-bottom: 6px; }
  .feature {
    position: absolute; left: 0; right: 0; top: 1040px;
    text-align: center; color: var(--paper);
  }
  .feature-label {
    font-size: 26px; font-weight: 700; letter-spacing: .1em;
    text-shadow: 0 0 4px rgba(0,0,0,.8);
  }
  .feature-text {
    display: block; margin-top: 6px;
    font-size: 62px; font-weight: 900; letter-spacing: -.01em;
    -webkit-text-stroke: 3px var(--ink); paint-order: stroke fill;
    text-shadow: 0 3px 6px rgba(0,0,0,.45);
  }
</style>
</head>
<body>
<main class="cover">
  <div class="cover-photo" role="img" aria-label="明るいリビングの写真:白い壁とソファ、手前に木製トランクのローテーブル"></div>

  <header class="masthead">
    <p class="masthead-kana">[ペブル・マガジン]</p>
    <span class="masthead-issue">vol.4 2021</span>
    <h2 class="masthead-name">
      <span class="word-main">Pebble</span>
      <span class="word-sub">magazine</span>
    </h2>
  </header>

  <ul class="topics">
    <li>家づくりの補助金</li>
    <li>4月に省エネ説明義務化</li>
    <li>IoT住宅の現在</li>
  </ul>

  <h1 class="title">
    <span class="title-line">後悔しない</span>
    <span class="title-line">住まい手配</span>
    <span class="title-line">ガイド決定版</span>
  </h1>
  <p class="title-en">How to plan the right home with no regrets</p>
  <p class="title-year">2021</p>

  <div class="badge">
    <svg width="40" height="36" viewBox="0 0 40 36" aria-hidden="true">
      <path d="M4 18 L20 4 L36 18 M9 14 V32 H31 V14" fill="none" stroke="#1b1b1b" stroke-width="3" stroke-linejoin="round"/>
      <rect x="17" y="22" width="6" height="10" fill="#1b1b1b"/>
    </svg>
    <span>コロナ対応住宅</span>
    <span>チェックリスト</span>
    <span>付き!</span>
  </div>

  <section class="feature">
    <p class="feature-label">[特集]</p>
    <p class="feature-text">三世代でつなぐ暮らし設計</p>
  </section>
</main>
</body>
</html>
```